Business Card design for amazing new Dental Office

Please read this brief closely!

Our client is a modern new dental office/
They love their new logo.
Now it's time to create a business card for them.

It should be a two sided card:
Side one should have the logo and name and maybe a color background or design.
Side two should have all the contact information which is here:

Trevor Lindqvist, D.D.S
General and Cosmetic Dentistry
4187 W. Pinecrest Avenue
Ventura, CA 93011
(805) 912-4386
drtrevor@bluefernsmiles-example.com
www.bluefernsmiles-example.com

Feel free to arrange that info as you like and to style both sides of the card according to your creativity. This is a chance for you to show your design skills!

Client is open to font choices and is looking for a style that is amazing and premium. Colors can be selected from the logo, or any variation of those.

You will not win this contest with a less than beautiful card design so please feel free to make multiple submissions.

Logo files attached and please message me with any questions.
Thanks!

Target Market(s)

Families and Professionals seeking dental services

Industry/Entity Type

Dental

Contact Information for Business Card

Logo, style, contact info as per the brief

Font styles to use
Sans Serif

Requirements
Must have
• Client's logo and contact details as per brief
Nice to have
• Unique style reflecting high end dental clinic near the beach
Should not have
• Must not look like a template

```html
<!DOCTYPE html>
<html lang="en">
<head>
<meta charset="utf-8">
<title>Blue Fern Smiles – Business Card</title>
<link rel="stylesheet" href="https://fonts.googleapis.com/css2?family=Josefin+Sans:wght@400;600&family=Questrial&display=swap">
<style>
  :root {
    --canvas-bg: #c8c8c8;
    --card-white: #ffffff;
    --sky: #dcebf7;
    --sea-light: #7fd0e4;
    --sea-deep: #1f9bc4;
    --sand: #efe3d2;
    --name-blue: #3aaee8;
    --text-grey: #8a8a8a;
    --brand-grey: #9aa3a8;
    --brand-sub-grey: #8f979c;
    --brand-teal: #5fbdb8;
    --icon-blue: #3aaee8;
  }
  * { margin: 0; padding: 0; box-sizing: border-box; }
  html, body { width: 1200px; height: 1000px; overflow: hidden; }
  body { background: var(--canvas-bg); position: relative; font-family: "Questrial", sans-serif; }

  .card { position: absolute; width: 606px; height: 346px; overflow: hidden; }

  /* Front side */
  .card-front { left: 99px; top: 113px; }
  .front-scene {
    position: absolute; inset: 0;
    background: linear-gradient(180deg,
      var(--sky) 0%, #e9f2f9 38%,
      var(--sea-light) 40%, var(--sea-deep) 62%,
      #bfe3ee 78%, var(--sand) 90%, #d9c8ae 100%);
  }
  .front-brand {
    position: absolute; left: 0; right: 0; top: 198px;
    text-align: center; color: var(--brand-grey);
    font-family: "Questrial", sans-serif; font-weight: 400;
  }
  .front-brand .brand-main { display: block; font-size: 29px; line-height: 32px; letter-spacing: 3px; }
  .front-brand .brand-sub {
    display: block; font-size: 15px; line-height: 18px; letter-spacing: 11px;
    margin-top: 6px; color: var(--brand-sub-grey);
  }

  /* Back side */
  .card-back { left: 492px; top: 531px; background: var(--card-white); }
  .holder-name {
    position: absolute; left: 30px; top: 58px;
    font-family: "Josefin Sans", sans-serif; font-weight: 600;
    font-size: 28px; color: var(--name-blue); white-space: nowrap;
  }
  .holder-title {
    position: absolute; left: 30px; top: 97px;
    font-size: 12.5px; letter-spacing: 2.5px; color: var(--text-grey); white-space: nowrap;
  }
  .contact-row {
    position: absolute; left: 30px; display: flex; align-items: flex-start;
    gap: 9px; color: var(--text-grey); font-size: 17.5px; line-height: 23px; white-space: nowrap;
  }
  .contact-row svg { flex: none; margin-top: 3px; }
  .row-address { top: 159px; }
  .row-email { top: 252px; }
  .row-web { top: 275px; }

  .back-brand {
    position: absolute; left: 372px; top: 130px; width: 220px;
    display: flex; align-items: center; gap: 12px;
    color: var(--brand-teal); font-family: "Questrial", sans-serif;
    font-weight: 400; font-size: 26px; line-height: 32px; letter-spacing: 1px;
  }
  .back-brand .brand-dot {
    flex: none; width: 16px; height: 16px; border-radius: 50%; background: var(--brand-teal);
  }
</style>
</head>
<body>

  <section class="card card-front">
    <div class="front-scene" role="img" aria-label="Painted view of a sunny beach with ocean, sand and palm trees"></div>
    <div class="front-brand">
      <span class="brand-main">BLUE FERN</span>
      <span class="brand-sub">SMILES</span>
    </div>
  </section>

  <section class="card card-back">
    <h1 class="holder-name">Trevor Lindqvist, D.D.S</h1>
    <p class="holder-title">GENERAL AND COSMETIC DENTISTRY</p>

    <div class="contact-row row-address">
      <svg width="12" height="18" viewBox="0 0 12 18" aria-hidden="true">
        <path d="M6 0C2.7 0 0 2.6 0 5.9 0 10.3 6 18 6 18s6-7.7 6-12.1C12 2.6 9.3 0 6 0z" fill="var(--icon-blue)"/>
        <circle cx="6" cy="6" r="2.3" fill="#fff"/>
      </svg>
      <p>4187 W. Pinecrest Avenue<br>Ventura, CA 93011<br>(805) 912-4386</p>
    </div>

    <div class="contact-row row-email">
      <svg width="16" height="12" viewBox="0 0 16 12" aria-hidden="true">
        <rect x="0" y="0" width="16" height="12" fill="var(--icon-blue)"/>
        <path d="M0.5 0.5 8 7 15.5 0.5" fill="none" stroke="#fff" stroke-width="1.3"/>
      </svg>
      <p>drtrevor@bluefernsmiles-example.com</p>
    </div>

    <div class="contact-row row-web">
      <svg width="16" height="16" viewBox="0 0 16 16" aria-hidden="true">
        <g fill="none" stroke="var(--icon-blue)" stroke-width="1.4">
          <circle cx="8" cy="8" r="7"/>
          <ellipse cx="8" cy="8" rx="3" ry="7"/>
          <line x1="1" y1="8" x2="15" y2="8"/>
          <line x1="2" y1="4.5" x2="14" y2="4.5"/>
          <line x1="2" y1="11.5" x2="14" y2="11.5"/>
        </g>
      </svg>
      <p>www.bluefernsmiles-example.com</p>
    </div>

    <div class="back-brand">
      <span class="brand-dot"></span>
      <span>Blue Fern<br>Smiles</span>
    </div>
  </section>

</body>
</html>
```